kn stationary
knbizcards
Simple
Harold T. Pemberly, PhD
CEO
218 Copperfield Lane, Suite 300 Jackson, MS 39211
htp@kestonnetworksllc.com
www.kestonnetworksllc.com

```html
<!DOCTYPE html>
<html lang="en">
<head>
<meta charset="utf-8">
<title>Keston Networks – Business Card</title>
<link href="https://fonts.googleapis.com/css2?family=Michroma&family=Open+Sans:wght@400;700&display=swap" rel="stylesheet">
<style>
  :root {
    --backdrop: #e9e6e1;
    --card: #ffffff;
    --ink: #222222;
    --ink-soft: #555555;
    --accent: #a3181d;
    --rule: #d6d6d6;
  }
  * { margin: 0; padding: 0; box-sizing: border-box; }
  html, body {
    width: 1200px; height: 778px; overflow: hidden;
    background: var(--backdrop);
    font-family: "Open Sans", Arial, sans-serif;
    color: var(--ink);
  }
  .card {
    position: absolute; left: 50px; top: 139px;
    width: 1100px; height: 500px;
    background: var(--card);
    border-radius: 34px;
    box-shadow: 0 6px 18px rgba(0,0,0,0.18);
  }
  .brand {
    position: absolute; left: 0; right: 0; top: 120px;
    display: flex; justify-content: center; align-items: center; gap: 22px;
  }
  .brand-dot {
    width: 26px; height: 26px; border-radius: 50%;
    background: var(--accent);
  }
  .brand-name {
    font-family: "Michroma", "Open Sans", sans-serif;
    font-size: 44px; letter-spacing: 2px;
    color: var(--ink);
  }
  .identity {
    position: absolute; right: 696px; top: 300px;
    text-align: right;
  }
  .person-name { font-size: 31px; font-weight: 700; color: var(--accent); line-height: 40px; }
  .person-title { font-size: 25px; color: var(--ink-soft); line-height: 36px; margin-bottom: 12px; }
  .address { font-size: 25px; line-height: 36px; color: var(--ink); }
  .divider {
    position: absolute; left: 462px; top: 298px;
    width: 2px; height: 170px; background: var(--rule);
  }
  .contacts {
    position: absolute; left: 504px; top: 294px;
    list-style: none;
  }
  .contacts li {
    display: flex; align-items: center; gap: 14px;
    font-size: 24px; line-height: 33px; color: var(--ink);
  }
  .contacts svg { width: 18px; height: 18px; fill: var(--accent); flex: none; }
</style>
</head>
<body>
  <main class="card">
    <div class="brand">
      <span class="brand-dot"></span>
      <span class="brand-name">KESTON NETWORKS</span>
    </div>

    <section class="identity">
      <p class="person-name">Harold T. Pemberly, PhD</p>
      <p class="person-title">CEO</p>
      <p class="address">218 Copperfield Lane, Suite 300<br>Jackson, MS 39211</p>
    </section>

    <div class="divider"></div>

    <ul class="contacts">
      <li><svg viewBox="0 0 20 20"><path d="M5 2l3 4-2 2c1 2 3 4 5 5l2-2 4 3-2 4C8 18 2 12 2 4z"/></svg>601-555-0142</li>
      <li><svg viewBox="0 0 20 20"><rect x="5" y="1" width="10" height="18" rx="2"/><rect x="7" y="4" width="6" height="9" fill="#fff"/></svg>601-555-0187</li>
      <li><svg viewBox="0 0 20 20"><rect x="5" y="2" width="10" height="6"/><rect x="2" y="8" width="16" height="8" rx="1"/><rect x="5" y="13" width="10" height="5" fill="#fff" stroke="#a3181d" stroke-width="1.5"/></svg>601-555-0163</li>
      <li><svg viewBox="0 0 20 20"><rect x="1.5" y="4" width="17" height="12" fill="none" stroke="#a3181d" stroke-width="2"/><path d="M2 5l8 6 8-6" fill="none" stroke="#a3181d" stroke-width="2"/></svg>htp@kestonnetworksllc.com</li>
      <li><svg viewBox="0 0 20 20"><circle cx="10" cy="10" r="8.5"/><path d="M1.5 10h17M10 1.5c-4 4-4 13 0 17M10 1.5c4 4 4 13 0 17" fill="none" stroke="#fff" stroke-width="1.3"/></svg>www.kestonnetworksllc.com</li>
    </ul>
  </main>
</body>
</html>
```